new roofing company card

New primary business card for roofing company.

Industry/Entity Type

Residential roofing/Specializing in Asphalt and Standing seam metal roofing

Contact Information for Business Card

Phone number is: 555 471 2086 Email: support@halvenshingleworks.example website: www.halvenshingleworks.example

Colors
EB3D1F
EC4F4E
F09395
F8D3D4
FCEDEE

```html
<!DOCTYPE html>
<html lang="en">
<head>
<meta charset="utf-8">
<title>Halven Shingleworks — Business Card</title>
<link href="https://fonts.googleapis.com/css2?family=Cinzel:wght@600&family=Montserrat:wght@500&display=swap" rel="stylesheet">
<style>
  :root {
    --backdrop: #e4e4e4;
    --card: #ffffff;
    --ink: #231f20;
    --brand-red: #b81e23;
    --shadow: rgba(0, 0, 0, 0.18);
  }
  * { box-sizing: border-box; margin: 0; padding: 0; }
  html, body {
    width: 1200px; height: 900px; overflow: hidden;
    background: var(--backdrop);
  }
  .canvas { position: relative; width: 1200px; height: 900px; }
  .card {
    position: absolute; width: 560px; height: 320px;
    background: var(--card); overflow: hidden;
    box-shadow: 0 14px 30px var(--shadow);
  }
  .card--front { left: 60px; top: 100px; }
  .card--back { left: 580px; top: 470px; }

  .wordmark {
    display: flex; align-items: center; justify-content: center; gap: 12px;
    font-family: "Cinzel", serif; font-weight: 600;
    color: var(--ink); letter-spacing: 0.02em; white-space: nowrap;
  }
  .wordmark__square { width: 16px; height: 16px; background: var(--brand-red); flex: none; }
  .card--front .wordmark { position: absolute; inset: 0; font-size: 34px; }
  .card--back .wordmark {
    position: absolute; left: 0; right: 0; top: 48px; font-size: 26px;
  }
  .card--back .wordmark__square { width: 13px; height: 13px; }

  .contact-list {
    position: absolute; left: 0; right: 0; top: 118px;
    list-style: none; display: flex; flex-direction: column; align-items: center; gap: 9px;
    font-family: "Montserrat", sans-serif; font-weight: 500; font-size: 14px; color: var(--ink);
  }
  .contact-list li { display: flex; align-items: center; gap: 7px; }
  .contact-icon { width: 16px; height: 16px; flex: none; }

  .card__band {
    position: absolute; left: 0; right: 0; bottom: 0; height: 14px; background: var(--ink);
  }
  .card__tab {
    position: absolute; left: 215px; width: 255px; bottom: 0; height: 78px;
    background: var(--brand-red); border-radius: 40px 40px 0 0;
    border: 3px solid var(--card); border-bottom: none;
  }
</style>
</head>
<body>
<main class="canvas">
  <section class="card card--front" aria-label="Card front">
    <div class="wordmark"><span class="wordmark__square"></span>Halven Shingleworks</div>
  </section>

  <section class="card card--back" aria-label="Card back">
    <div class="wordmark"><span class="wordmark__square"></span>Halven Shingleworks</div>
    <ul class="contact-list">
      <li>
        <svg class="contact-icon" viewBox="0 0 16 16" aria-hidden="true">
          <rect width="16" height="16" rx="2" fill="var(--brand-red)"/>
          <path d="M4 5.5c0-1 1-1.5 4-1.5s4 .5 4 1.5v1h-2.2v-1H6.2v1H4z M5 8h6l1 4H4z" fill="#fff"/>
        </svg>
        555 471 2086
      </li>
      <li>
        <svg class="contact-icon" viewBox="0 0 16 16" aria-hidden="true">
          <rect width="16" height="16" rx="2" fill="var(--brand-red)"/>
          <rect x="3.5" y="5" width="9" height="6.5" fill="none" stroke="#fff" stroke-width="1.1"/>
          <path d="M3.5 5 8 8.7 12.5 5" fill="none" stroke="#fff" stroke-width="1.1"/>
        </svg>
        support@halvenshingleworks.example
      </li>
      <li>
        <svg class="contact-icon" viewBox="0 0 16 16" aria-hidden="true">
          <rect width="16" height="16" rx="2" fill="var(--brand-red)"/>
          <circle cx="8" cy="8" r="4.3" fill="none" stroke="#fff" stroke-width="1.1"/>
          <path d="M3.7 8h8.6 M8 3.7c-2 2.6-2 6 0 8.6 M8 3.7c2 2.6 2 6 0 8.6" fill="none" stroke="#fff" stroke-width="0.9"/>
        </svg>
        www.halvenshingleworks.example
      </li>
    </ul>
    <div class="card__band"></div>
    <div class="card__tab"></div>
  </section>
</main>
</body>
</html>
```